Labels for Bees Wax Candles & Honey Jars

We need labels for jars of natural honey. Most of our jars are square and the labels about 2" by 2".

Also we make bees wax candles of various sizes. We wish to wrap th enables around the circular candles which are between 2" and 3" in diameter... thus another have inch per label so they can be attached adhesively. The candles also vary in height... therefor th enables need to be 1.5", 2" and 3" in height.

We ar elooking for a very artistic and simple label that may include vibrant colors.
The name of our company must be displayed.. Candles by Morrow and for the Honey.... Morrow's All Natural Honey
Updates

The labels will be used for both Honey Jars as well as Bees Wax candles. There will be various sizes but that is something that can be adjusted after the initial design is approved. The Honey Jars should read "Natural Honey by Morrow" and the Candle labels should read "Natural Bees Wax Candles by Morrow" I am interested in simple, colorful, legible, and arty labels that pertain to bees and the natural environment. Hope this helps. We may also use a similar design on our web page. The size of the label on the honey will be 2" by 2" and the candles will vary.

Target Market(s)

Individual that purchase natural and organic products.

Requirements
Must have
• Labels should be very creative but legible and the emphasis on the candles should be all natural bees wax and the emphasis on the honey should be all natural honey. We are talking about the same design but different sizes and names.
Nice to have
• brillant colors and artistic

```html
<!DOCTYPE html>
<html lang="en">
<head>
<meta charset="UTF-8">
<title>Morrow's All Natural Honey — Label Colourways</title>
<link href="https://fonts.googleapis.com/css2?family=Dancing+Script:wght@700&family=Open+Sans:wght@700&display=swap" rel="stylesheet">
<style>
  :root {
    --canvas-bg: #111111;
    --comb-gold: #f0b23a;
    --comb-amber: #d9882a;
    --comb-red: #9a3d22;
    --hive-cream: #fbf1d6;
    --hive-shade: #e6c98d;
    --gold-text: #f6c935;
    --pale-text: #fbe7a0;
    --ink: #1c1206;
    --panel-brown: #4a2510;
    --panel-orange: #f09a2a;
    --panel-amber: #f7b84a;
    --panel-green: #3f6b35;
  }
  * { box-sizing: border-box; margin: 0; padding: 0; }
  html, body {
    width: 1200px;
    height: 1200px;
    overflow: hidden;
    background: var(--canvas-bg);
  }
  .label-sheet {
    width: 1200px;
    height: 1200px;
    display: grid;
    grid-template-columns: repeat(2, 460px);
    grid-template-rows: repeat(2, 460px);
    gap: 90px;
    justify-content: center;
    align-content: center;
  }
  .honey-label {
    position: relative;
    width: 460px;
    height: 460px;
  }
  .comb-border {
    position: absolute;
    inset: 0;
    background: linear-gradient(135deg, var(--comb-gold) 0%, var(--comb-amber) 45%, var(--comb-red) 100%);
  }
  .label-panel {
    position: absolute;
    inset: 46px;
    display: flex;
    flex-direction: column;
    align-items: center;
    justify-content: space-between;
    padding: 16px 12px 22px;
  }
  .brand-name {
    font-family: 'Dancing Script', cursive;
    font-weight: 700;
    font-size: 78px;
    line-height: 1;
    color: var(--gold-text);
  }
  .hive-art {
    width: 240px;
    height: 150px;
    border-radius: 6px;
    background: linear-gradient(180deg, var(--hive-cream), var(--hive-shade));
  }
  .product-line {
    font-family: 'Open Sans', sans-serif;
    font-weight: 700;
    font-size: 24px;
    line-height: 1.2;
    color: var(--gold-text);
  }
  .label-brown .label-panel { background: var(--panel-brown); }
  .label-orange .label-panel { background: var(--panel-orange); }
  .label-orange .brand-name,
  .label-orange .product-line { color: var(--pale-text); }
  .label-amber .label-panel { background: var(--panel-amber); }
  .label-amber .brand-name { color: var(--pale-text); }
  .label-amber .product-line { color: var(--ink); }
  .label-green .label-panel { background: var(--panel-green); }
</style>
</head>
<body>
  <main class="label-sheet">
    <section class="honey-label label-brown">
      <div class="comb-border" role="img" aria-label="Honeycomb pattern border in golds and reds"></div>
      <div class="label-panel">
        <h1 class="brand-name">Morrow's</h1>
        <div class="hive-art" role="img" aria-label="Illustration of a cream beehive with two bees"></div>
        <p class="product-line">All Natural Honey</p>
      </div>
    </section>
    <section class="honey-label label-orange">
      <div class="comb-border" role="img" aria-label="Honeycomb pattern border in golds and reds"></div>
      <div class="label-panel">
        <h2 class="brand-name">Morrow's</h2>
        <div class="hive-art" role="img" aria-label="Illustration of a cream beehive with two bees"></div>
        <p class="product-line">All Natural Honey</p>
      </div>
    </section>
    <section class="honey-label label-amber">
      <div class="comb-border" role="img" aria-label="Honeycomb pattern border in golds and reds"></div>
      <div class="label-panel">
        <h2 class="brand-name">Morrow's</h2>
        <div class="hive-art" role="img" aria-label="Illustration of a cream beehive with two bees"></div>
        <p class="product-line">All Natural Honey</p>
      </div>
    </section>
    <section class="honey-label label-green">
      <div class="comb-border" role="img" aria-label="Honeycomb pattern border in golds and reds"></div>
      <div class="label-panel">
        <h2 class="brand-name">Morrow's</h2>
        <div class="hive-art" role="img" aria-label="Illustration of a cream beehive with two bees"></div>
        <p class="product-line">All Natural Honey</p>
      </div>
    </section>
  </main>
</body>
</html>
```